Upscale business cards needed for family office

We would like professional business cards created for employees of our family office. Relatively simple and straightforward, but also with a unique element to set them apart. Probably stick with neutral and simple colors that mesh well with the colors in the logo. We need space for the traditional elements, including name, title, address, email/phone number.

Industry/Entity Type

Business

Contact Information for Business Card

Space for name, title, phone number, email, address

```html
<!DOCTYPE html>
<html lang="en">
<head>
<meta charset="utf-8">
<title>R&amp;T Family Office – Business Cards</title>
<link rel="stylesheet" href="https://fonts.googleapis.com/css2?family=Tinos:wght@400;700&display=swap">
<style>
  :root {
    --page-bg: #e6e7e9;
    --card-bg: #ffffff;
    --ink: #4f5a63;
    --ink-soft: #6b757d;
    --accent-blue: #2a93c4;
    --rule: #d5d9dd;
    --pier-sky: #f4f6fa;
    --pier-haze: #e2e8f1;
    --pier-water: #d6dfeb;
    --pier-fade: #f1f4f8;
  }
  * { box-sizing: border-box; margin: 0; padding: 0; }
  html, body {
    width: 1200px; height: 800px; overflow: hidden;
    background: var(--page-bg);
    font-family: "Tinos", "Times New Roman", serif;
    color: var(--ink);
  }
  .stage { position: relative; width: 1200px; height: 800px; }
  .card {
    position: absolute; top: 257px;
    width: 500px; height: 286px;
    background: var(--card-bg);
    box-shadow: 0 6px 18px rgba(0,0,0,0.12);
    overflow: hidden;
  }
  .card--details { left: 80px; }
  .card--front { left: 620px; }

  .brand {
    display: flex; align-items: center; gap: 10px;
    font-size: 34px; font-weight: 400; color: var(--ink);
    letter-spacing: 1px;
  }
  .brand__square { width: 26px; height: 26px; background: var(--accent-blue); }
  .card--front .brand {
    position: absolute; left: 50%; top: 50%;
    transform: translate(-50%, -50%);
  }

  .pier-photo {
    position: absolute; left: 0; top: 100px; width: 100%; height: 150px;
    background: linear-gradient(172deg,
      var(--pier-sky) 0%,
      var(--pier-haze) 28%,
      var(--pier-water) 48%,
      var(--pier-haze) 66%,
      var(--pier-fade) 84%,
      rgba(255,255,255,0) 100%);
  }
  .card--details .brand {
    position: absolute; left: 58px; top: 92px;
    font-size: 30px;
  }
  .divider {
    position: absolute; left: 238px; top: 70px;
    width: 1px; height: 130px; background: var(--rule);
  }
  .contact { position: absolute; left: 258px; top: 90px; }
  .contact__name { font-size: 22px; font-weight: 700; color: var(--ink); }
  .contact__title { font-size: 12px; color: var(--accent-blue); margin-bottom: 8px; }
  .contact__list { list-style: none; }
  .contact__item {
    display: flex; align-items: center; gap: 7px;
    font-size: 12px; color: var(--ink-soft); line-height: 17px;
  }
  .contact__item svg { width: 10px; height: 10px; fill: var(--ink); }
  .address {
    position: absolute; left: 0; right: 0; bottom: 24px;
    text-align: center; font-size: 12px; color: var(--ink-soft);
  }
</style>
</head>
<body>
<main class="stage">
  <section class="card card--details">
    <div class="pier-photo" role="img" aria-label="Faint, washed-out photo of a wooden pier on posts over calm water"></div>
    <div class="brand"><span class="brand__square"></span><span class="brand__name">R&amp;T</span></div>
    <div class="divider"></div>
    <div class="contact">
      <p class="contact__name">Daniel Hart</p>
      <p class="contact__title">Managing director</p>
      <ul class="contact__list">
        <li class="contact__item">
          <svg viewBox="0 0 10 10"><path d="M2 0.5 L3.8 2.8 L2.8 3.8 Q4 6 6.2 7.2 L7.2 6.2 L9.5 8 L8 9.5 Q3.5 9 0.5 2 Z"/></svg>
          0775-3812-4409
        </li>
        <li class="contact__item">
          <svg viewBox="0 0 10 10"><rect x="2" y="0.5" width="6" height="9" rx="1"/></svg>
          0713-6240-5518
        </li>
        <li class="contact__item">
          <svg viewBox="0 0 10 10"><rect x="0.5" y="2" width="9" height="6.5" rx="0.6"/></svg>
          dhart@rtfamily.com
        </li>
        <li class="contact__item">
          <svg viewBox="0 0 10 10"><path d="M0.5 1.5 H9.5 V7.5 H0.5 Z M1.5 2.5 V6.5 H8.5 V2.5 Z M3 8.5 H7 V9.5 H3 Z"/></svg>
          rtfamily.com
        </li>
      </ul>
    </div>
    <p class="address">2200 Harbor Lane, Suite 300, City, State, Zip Code</p>
  </section>

  <section class="card card--front">
    <div class="brand"><span class="brand__square"></span><span class="brand__name">R&amp;T</span></div>
  </section>
</main>
</body>
</html>
```